Medical Billing - Professional Marketing Flier

We are needing help designing a clean and professional looking easy to read marketing flier for a medical billing practice. The text needs to be large enough to print. We are looking for a 5.5 x 8.5 design that we can edit the text as needed. I have included our logo and what we initially want it to say. Please keep in mind, we also want our logo and contact details on the flier. Let me know if you have any questions.

```html
<!DOCTYPE html>
<html lang="en">
<head>
<meta charset="utf-8">
<title>Vega Medical Billing – Flier</title>
<link rel="stylesheet" href="https://fonts.googleapis.com/css2?family=Roboto+Condensed:ital,wght@0,400;0,500;0,700;1,400;1,700&display=swap">
<style>
  :root {
    --magenta: #c2519f;
    --blue: #29a8e0;
    --blue-deep: #1b8ccf;
    --ink: #2f2f33;
    --page: #ffffff;
    --backdrop: #eeeeef;
  }
  * { box-sizing: border-box; margin: 0; padding: 0; }
  html, body { width: 1200px; height: 1200px; overflow: hidden; }
  body {
    background: var(--backdrop);
    font-family: "Roboto Condensed", "Arial Narrow", sans-serif;
    color: var(--ink);
    position: relative;
  }
  .flier {
    position: absolute;
    left: 232px; top: 31px;
    width: 736px; height: 1137px;
    background: var(--page);
    overflow: hidden;
  }
  .shapes { position: absolute; inset: 0; width: 736px; height: 1137px; }
  .brand {
    position: absolute; left: 50px; top: 150px;
    display: flex; align-items: center; gap: 10px;
    font-size: 28px; font-weight: 500; color: var(--magenta);
    letter-spacing: 0.5px; line-height: 1;
  }
  .brand-dot { width: 12px; height: 12px; border-radius: 50%; background: var(--magenta); }
  .section-title {
    position: absolute;
    font-size: 33px; font-weight: 700; font-style: italic;
    letter-spacing: 0.5px; line-height: 1;
    color: var(--magenta);
  }
  .section-title--light { color: #fff; }
  .body-copy {
    position: absolute;
    font-size: 13.2px; line-height: 16.4px; color: var(--ink);
  }
  .title-billing { left: 46px; top: 262px; }
  .copy-billing { left: 46px; top: 314px; width: 318px; }
  .title-aging { left: 46px; top: 550px; }
  .copy-aging { left: 194px; top: 532px; width: 500px; }
  .title-credentialing { left: 46px; top: 705px; }
  .copy-credentialing { left: 46px; top: 764px; width: 332px; }
  .contact-title {
    position: absolute; left: 0; width: 736px; top: 942px;
    text-align: center; color: #fff;
    font-size: 30px; font-weight: 700; font-style: italic; line-height: 34px;
  }
  .contact-lead {
    position: absolute; left: 48px; width: 640px; top: 1002px;
    text-align: center;
    font-size: 15.5px; line-height: 19px; font-weight: 700; font-style: italic;
  }
  .contact-note {
    position: absolute; left: 48px; width: 640px; top: 1064px;
    text-align: center; font-size: 12.5px; line-height: 15.5px;
  }
</style>
</head>
<body>
  <main class="flier">
    <svg class="shapes" viewBox="0 0 736 1137">
      <defs>
        <linearGradient id="photo-office" x1="0" y1="0" x2="1" y2="1">
          <stop offset="0" stop-color="#f2f1ee"/>
          <stop offset="0.55" stop-color="#dfe3e6"/>
          <stop offset="1" stop-color="#c9cfd4"/>
        </linearGradient>
        <linearGradient id="photo-tablet" x1="0" y1="0" x2="1" y2="1">
          <stop offset="0" stop-color="#dde3e8"/>
          <stop offset="0.6" stop-color="#c8d2da"/>
          <stop offset="1" stop-color="#e9e4df"/>
        </linearGradient>
        <linearGradient id="contact-wash" x1="0" y1="0" x2="0" y2="1">
          <stop offset="0" stop-color="#ffffff"/>
          <stop offset="0.35" stop-color="#eeeaf5"/>
          <stop offset="1" stop-color="#e4e9f4"/>
        </linearGradient>
        <linearGradient id="banner-fade" x1="0" y1="0" x2="1" y2="0">
          <stop offset="0" stop-color="#29a8e0" stop-opacity="0"/>
          <stop offset="0.25" stop-color="#29a8e0"/>
          <stop offset="0.75" stop-color="#29a8e0"/>
          <stop offset="1" stop-color="#29a8e0" stop-opacity="0"/>
        </linearGradient>
      </defs>

      <rect class="contact-backdrop" x="0" y="920" width="736" height="217" fill="url(#contact-wash)"/>

      <polygon class="accent-hex-blue" points="475,111 736,111 736,516 489,516 394,313" fill="var(--blue)"/>
      <polygon class="photo-doctor" role="img" aria-label="Photo of a doctor in a white coat writing notes beside a tablet"
        points="405,32 671,32 736,198 671,365 405,365 347,198" fill="url(#photo-office)"/>

      <line x1="310" y1="277" x2="352" y2="277" stroke="var(--magenta)" stroke-width="3"/>
      <circle cx="360" cy="277" r="9" fill="var(--magenta)"/>

      <polygon class="aging-hex" points="0,475 135,475 173,567 135,662 0,662" fill="var(--blue)"/>
      <polygon class="aging-hex-small" points="104,617 137,617 151,644 137,671 104,671 90,644" fill="var(--blue-deep)"/>

      <polygon class="photo-consult" role="img" aria-label="Photo of a clinician showing a form on a tablet during a consultation"
        points="459,637 662,637 718,765 662,894 459,894 401,765" fill="url(#photo-tablet)"/>
      <polygon class="accent-hex-magenta" points="421,657 462,657 482,698 462,738 421,738 401,698" fill="var(--magenta)" opacity="0.9"/>

      <line x1="293" y1="721" x2="354" y2="721" stroke="var(--magenta)" stroke-width="3"/>
      <circle cx="362" cy="721" r="9" fill="var(--magenta)"/>

      <rect class="contact-banner" x="150" y="940" width="440" height="38" fill="url(#banner-fade)"/>
      <rect class="footer-bar" x="178" y="1126" width="378" height="11" fill="var(--magenta)"/>
    </svg>

    <div class="brand"><span class="brand-dot"></span>Vega Medical Billing</div>

    <h2 class="section-title title-billing">MEDICAL BILLING</h2>
    <p class="body-copy copy-billing">Would you prefer to spend time focusing on your clients and running your practice rather than trying to stay up to speed with the constantly changing medical billing rules and regulations? Let us help you by managing your medical billing and dealing with the insurance companies on your behalf! We work with you to tailor the entire medical billing process to suit your practices needs while making it as smooth and painless as possible.</p>

    <h2 class="section-title section-title--light title-aging">AGING</h2>
    <p class="body-copy copy-aging">Are you leaving money on the table? Are you able to do the follow-through needed to keep your aging in check and more money flowing into your practice? Are you uncertain about how to get insurance to pay on claims that should be covered but for some reason they decided not to? We can clean up your aging, reduce the amount of time it takes for claims to pay out, and we can keep your aging to a minimum.</p>

    <h2 class="section-title title-credentialing">CREDENTIALING</h2>
    <p class="body-copy copy-credentialing">Are you wanting to get contracted with insurance companies but aren't sure how to go about it? Are you wanting to expand your client base by having the option to bill insurance? Let us take the confusion out of what can seem like a daunting task! We can get you and your practitioners contracted with the insurance companies of your choice and help you navigate through the process every step of the way!</p>

    <h2 class="contact-title">CONTACT US</h2>
    <p class="contact-lead">If any of these processes are something you would like our help with or to consult with us on, please email us or give us a call!</p>
    <p class="contact-note">We specialize in billing and contracting for Nutritionists and Dietitians. We would love to help you expand your business and take the pain and frustration out of billing so you can focus on your clients.</p>
  </main>
</body>
</html>
```